Brisk Mend's Blow Their Mind Website

We own a group of cell phone and tablet repair shops in the bay area that is emerging into the mobile device insurance industry and want to develop a site that is clean, organized, and efficient at communicating who we are, the services we provide and the positive feedback we have been getting from our clients. As we enter into this new field of business, Our goal is to attract larger corporate accounts.

We want our home screen to have a big focus on the protection plan for the devices right away much like the home screen from these links:

http://www.gadgetvault.com/

and also - https://us.keepitsnug.com/smartphone-protection.html

We also need to make our repair services clear, here is a website of a company that does repair and we want to highlight both ends of the business.

ww.fixnovo.com

So the home screen will include the tab categories at the top of the screen
home/ protection /repair /about /contact

The first portion will be protection and as you scroll down there will be the next section about repair and following that will be information about the company.

Target Market(s)

Individuals that would be looking for pricing, clients that come to our store, but ultimately the heavy hitters we would want to attract would be larger corporate accounts so the message we want to communicate is professional, organized and credible in the services we provide.

Industry/Entity Type

Cell Phone

Number of Pages Required

5+ page

Font styles to use
Serif

Colors
34a6d7

Requirements
Must have
• Eye catching, organized, with the wow factor that a business will look at our site and will be able to tell that we know what looks good and what grabs peoples attention. A large emphasis on the protection plan section like the links we provided and an organized home screen with the sections highlighted in the project description
• Tabs with links to different sections of the business such as protection that will go into detail about our protections plans and why our plan is best
• repair with a menu of the different prices we provide for different devices and services for that device
• an about us tab
• a contact us tab
Nice to have
• Artistic flow on the homescreen that the different sections flow together without looking too cookie cutter
• Wow factor
Should not have
• Clutter, confusion, disorganization, cheesy cookie cutter

```html
<!DOCTYPE html>
<html lang="en">
<head>
<meta charset="utf-8">
<title>Brisk Mend – Device Protection &amp; Repair</title>
<link href="https://fonts.googleapis.com/css2?family=Roboto:wght@400;500;700;900&display=swap" rel="stylesheet">
<style>
  :root{
    --brand:#34a6d7;
    --brand-bright:#1fb3ef;
    --brand-deep:#1c8fc4;
    --ink:#222;
    --muted:#666;
    --dark:#2a2a2a;
    --line:#dcdcdc;
    --white:#fff;
    --col-head:#8a8a8a;
  }
  *{box-sizing:border-box;margin:0;padding:0}
  html,body{width:896px;height:1200px;overflow:hidden}
  body{font-family:"Roboto",Arial,sans-serif;color:var(--ink);background:var(--white);position:relative}

  /* header */
  .site-header{height:30px;display:flex;align-items:center;justify-content:space-between;padding:0 170px 0 180px;background:var(--white)}
  .brand{display:flex;align-items:center;gap:6px;font-weight:700;font-size:15px;color:var(--brand)}
  .brand-dot{width:16px;height:16px;border-radius:50%;background:var(--brand)}
  .main-nav{display:flex;gap:12px;font-size:9px;color:var(--ink)}

  /* hero */
  .hero{position:relative;height:255px;overflow:hidden;color:var(--white);text-align:center}
  .hero-photo{position:absolute;inset:0;background:radial-gradient(ellipse at 50% 70%,#7fd3f5 0%,#3fb6ea 45%,#1e9ad2 100%)}
  .hero-content{position:relative;padding-top:45px}
  .hero h1{font-weight:700;font-size:30px;line-height:34px;letter-spacing:.5px}
  .hero p{width:380px;margin:10px auto 0;font-size:8px;line-height:11px}
  .btn-dark{display:inline-block;margin-top:14px;background:#111;color:var(--white);font-size:8px;font-weight:700;padding:8px 14px}

  /* about */
  .who{height:240px;position:relative;padding:18px 0 0}
  .who h2{text-align:center;font-size:20px;font-weight:900;letter-spacing:.5px}
  .who-rule{width:40px;height:2px;background:var(--brand);margin:5px auto 0}
  .who-text{position:absolute;left:170px;top:62px;width:290px;text-align:center;font-size:8px;line-height:12px;color:var(--muted)}
  .btn-brand{display:inline-block;margin-top:12px;background:var(--brand);color:var(--white);font-size:8px;font-weight:700;padding:7px 12px}
  .who-media{position:absolute;left:490px;top:62px;width:240px;height:125px;background:linear-gradient(135deg,#cfe9f6,#7cc2e4 55%,#3b8fb8)}

  /* features */
  .features{height:135px;display:flex;justify-content:center;gap:10px;padding-top:8px}
  .feature{width:110px;text-align:center;font-size:8px;color:var(--ink)}
  .feature-icon{width:54px;height:54px;margin:0 auto 8px;border:2px solid var(--brand);border-radius:50%;display:flex;align-items:center;justify-content:center}

  /* pricing */
  .pricing{height:230px;background:var(--dark);padding-top:12px}
  .pricing h2{text-align:center;color:var(--white);font-size:19px;font-weight:700;letter-spacing:.5px}
  .price-table{width:510px;margin:12px auto 0;border-collapse:collapse;background:var(--white);font-size:7px;color:var(--muted)}
  .price-table th{height:48px;background:var(--col-head);color:var(--white);font-weight:500;line-height:10px;font-size:7.5px}
  .price-table th.blank{background:var(--white)}
  .price-table th.featured{background:var(--brand)}
  .price-table td{height:18px;border-bottom:1px solid var(--line);text-align:center}
  .price-table td.label{text-align:left;padding-left:8px;width:138px;color:var(--ink)}
  .price-table td.featured{background:#eaf6fc}
  .tick{display:inline-block;width:10px;height:10px;border-radius:50%;background:var(--brand);position:relative;vertical-align:middle}
  .tick::after{content:"";position:absolute;left:3px;top:1.5px;width:3px;height:5px;border:solid var(--white);border-width:0 1.5px 1.5px 0;transform:rotate(45deg)}

  /* reviews */
  .reviews{height:220px;background:var(--brand-bright);color:var(--white);text-align:center;padding-top:14px}
  .reviews h2{font-size:12px;font-weight:700;letter-spacing:.5px}
  .reviewer-photo{width:58px;height:58px;border-radius:50%;margin:16px auto 0;border:3px solid var(--white);background:linear-gradient(160deg,#e6e6e6,#9a9a9a)}
  .reviewer-name{margin-top:8px;font-size:7px;font-weight:700;letter-spacing:1px}
  .review-text{width:360px;margin:8px auto 0;font-size:8px;line-height:12px}
  .dots{display:flex;gap:5px;justify-content:center;margin-top:12px}
  .dots span{width:5px;height:5px;border-radius:50%;background:rgba(255,255,255,.5)}
  .dots span.active{background:var(--white)}

  /* footer */
  .site-footer{height:90px;position:relative;background:var(--white)}
  .footer-row{display:flex;align-items:center;justify-content:space-between;padding:30px 170px 0 180px}
  .footer-nav{display:flex;gap:12px;font-size:9px}
  .social{display:flex;gap:6px}
  .social span{width:15px;height:15px;border-radius:50%;background:var(--brand)}
  .copyright{position:absolute;left:0;right:0;bottom:0;height:14px;background:var(--dark);color:#aaa;font-size:6px;line-height:14px;text-align:center}
</style>
</head>
<body>

<header class="site-header">
  <div class="brand"><span class="brand-dot"></span>Brisk Mend</div>
  <nav class="main-nav"><span>Home</span><span>About</span><span>Repair</span><span>Protect</span><span>Contact</span></nav>
</header>

<section class="hero">
  <div class="hero-photo" role="img" aria-label="Row of smartphones on a bright blue background"></div>
  <div class="hero-content">
    <h1>SMART PHONE PROTECT FROM<br>$5.00 A MONTH</h1>
    <p>Complete coverage for accidental damage, breakdowns and theft. Simple plans, fast claims and local repair experts ready to help you.</p>
    <span class="btn-dark">GET A QUOTE</span>
  </div>
</section>

<section class="who">
  <h2>WHO WE ARE</h2>
  <div class="who-rule"></div>
  <div class="who-text">
    <p>Brisk Mend began as a small group of repair shops in the bay area. Today our technicians fix thousands of phones and tablets every year, and we bring that same care to device protection. Every plan is backed by certified repairs, genuine parts and a team that answers the phone. From a single handset to a full corporate fleet, we keep your devices working.</p>
    <span class="btn-brand">READ MORE</span>
  </div>
  <div class="who-media" role="img" aria-label="Hand holding a smartphone playing a video"></div>
</section>

<section class="features">
  <div class="feature">
    <div class="feature-icon"><svg width="24" height="30" viewBox="0 0 24 30"><rect x="3" y="1" width="18" height="28" rx="3" fill="none" stroke="#34a6d7" stroke-width="2"/><circle cx="12" cy="25" r="1.5" fill="#34a6d7"/></svg></div>
    Damage Protection
  </div>
  <div class="feature">
    <div class="feature-icon"><svg width="24" height="28" viewBox="0 0 24 28"><path d="M12 2 C12 2 3 13 3 18 a9 9 0 0 0 18 0 C21 13 12 2 12 2Z" fill="none" stroke="#34a6d7" stroke-width="2"/></svg></div>
    Liquid &amp; Water Damage
  </div>
  <div class="feature">
    <div class="feature-icon"><svg width="28" height="28" viewBox="0 0 28 28"><circle cx="14" cy="14" r="5" fill="none" stroke="#34a6d7" stroke-width="2"/><circle cx="14" cy="14" r="10" fill="none" stroke="#34a6d7" stroke-width="2" stroke-dasharray="4 3"/></svg></div>
    Screen Replacement
  </div>
  <div class="feature">
    <div class="feature-icon"><svg width="28" height="28" viewBox="0 0 28 28"><rect x="3" y="5" width="22" height="20" rx="2" fill="none" stroke="#34a6d7" stroke-width="2"/><line x1="3" y1="11" x2="25" y2="11" stroke="#34a6d7" stroke-width="2"/><line x1="9" y1="2" x2="9" y2="8" stroke="#34a6d7" stroke-width="2"/><line x1="19" y1="2" x2="19" y2="8" stroke="#34a6d7" stroke-width="2"/></svg></div>
    Loss &amp; Theft Cover
  </div>
</section>

<section class="pricing">
  <h2>PRICE COMPARISON CHART</h2>
  <table class="price-table">
    <tr>
      <th class="blank"></th>
      <th>Competitor A<br>$8.99<br>/month</th>
      <th>Competitor B<br>$9.50<br>/month</th>
      <th class="featured">Brisk Mend<br>$5.00<br>/month</th>
    </tr>
    <tr><td class="label">Accidental damage</td><td><span class="tick"></span></td><td><span class="tick"></span></td><td class="featured"><span class="tick"></span></td></tr>
    <tr><td class="label">Mechanical breakdown</td><td><span class="tick"></span></td><td><span class="tick"></span></td><td class="featured"><span class="tick"></span></td></tr>
    <tr><td class="label">Service fee cost</td><td>$99 fee</td><td>$75 fee</td><td class="featured">No fee</td></tr>
    <tr><td class="label">Deductible</td><td>$50</td><td>$25</td><td class="featured">$0</td></tr>
    <tr><td class="label">Damage claim limits</td><td>$1,500</td><td>Device value</td><td class="featured">Unlimited</td></tr>
    <tr><td class="label">Replacement turnaround</td><td>5 days</td><td>3 days</td><td class="featured">Same day</td></tr>
    <tr><td class="label">Cancellation policy</td><td>Prorated refund</td><td>30 days</td><td class="featured">Cancel any time</td></tr>
  </table>
</section>

<section class="reviews">
  <h2>CUSTOMER REVIEWS</h2>
  <div class="reviewer-photo" role="img" aria-label="Portrait of a customer"></div>
  <div class="reviewer-name">DANIEL WHITMORE</div>
  <p class="review-text">Our office sends every cracked screen to Brisk Mend now. Repairs are quick, pricing is clear and the protection plan has already paid for itself twice this year.</p>
  <div class="dots"><span class="active"></span><span></span><span></span></div>
</section>

<footer class="site-footer">
  <div class="footer-row">
    <div class="brand"><span class="brand-dot"></span>Brisk Mend</div>
    <nav class="footer-nav"><span>Home</span><span>About</span><span>Repair</span><span>Protect</span><span>Contact</span></nav>
    <div class="social"><span></span><span></span><span></span></div>
  </div>
  <div class="copyright">© 2024 Brisk Mend. All rights reserved.</div>
</footer>

</body>
</html>
```